Brightwell Consulting Business Card Design

Business Card Design for Brightwell Consulting. Brightwell Consulting is a boutique consultancy based in Atlanta, GA., that specializes in marketing strategy, organization planning, and leadership development. We provide solutions for small businesses and startups as well as Summit 400 companies.

http://brightwellconsulting.example/

Target Market(s)

We provide solutions for small businesses and startups as well as Summit 400 companies.

Industry/Entity Type

Consulting

Contact Information for Business Card

Two sided business card with priority on contact information, logo, tag line (Guidance to Think Bigger, Act Bolder, Grow Further)

Colors

Designer to choose colors to be used in the design.

Requirements
Must have
• contact information, logo, tag line (Guidance to Think Bigger, Act Bolder, Grow Further)
• Simple no over communication.
Nice to have
• I would like to see different placements of logo and creative use of both sides of the card
Should not have
• Do not put too much information on the card.

```html
<!DOCTYPE html>
<html lang="en">
<head>
<meta charset="utf-8">
<title>Brightwell Consulting Business Card</title>
<link rel="stylesheet" href="https://fonts.googleapis.com/css2?family=Lato:wght@400;700&family=Yesteryear&display=swap">
<style>
  :root {
    --page: #d9d6d3;
    --card: #141414;
    --card-edge: #1d1d1d;
    --ink: #f4f4f4;
    --ink-soft: #c9c9c9;
    --ink-muted: #9a9a9a;
    --rule: #5a5a5a;
  }
  * { margin: 0; padding: 0; box-sizing: border-box; }
  html, body {
    width: 1200px; height: 769px; overflow: hidden;
    background: var(--page);
    font-family: "Lato", Arial, sans-serif;
  }
  .canvas {
    width: 1200px; height: 769px;
    display: flex; align-items: center; justify-content: center; gap: 40px;
  }
  .card {
    width: 540px; height: 309px;
    background: linear-gradient(160deg, var(--card-edge), var(--card));
    border-radius: 4px;
    box-shadow: 0 10px 28px rgba(0,0,0,.28);
    position: relative;
    color: var(--ink);
    overflow: hidden;
  }
  .wordmark {
    display: flex; align-items: center; gap: 10px;
    font-weight: 700; color: var(--ink);
    line-height: 1.05;
  }
  .wordmark-mark {
    width: 14px; height: 14px; background: var(--ink); flex: none;
  }
  .wordmark-text { display: block; }

  /* Front */
  .card-front { display: flex; align-items: center; }
  .front-brand {
    width: 250px; height: 100%;
    display: flex; align-items: center; justify-content: center;
  }
  .front-brand .wordmark-text { font-size: 26px; }
  .divider {
    width: 1px; height: 190px;
    background: linear-gradient(to bottom, transparent, var(--rule), transparent);
  }
  .front-details { padding-left: 30px; }
  .person-name {
    font-family: "Yesteryear", cursive;
    font-size: 30px; color: var(--ink-muted);
    line-height: 1;
  }
  .person-title {
    font-size: 14px; color: var(--ink-soft); margin-top: 6px; margin-bottom: 16px;
  }
  .contact-list { list-style: none; }
  .contact-item {
    display: flex; align-items: center; gap: 10px;
    font-size: 13px; color: var(--ink-soft); margin-bottom: 6px;
    white-space: nowrap;
  }
  .contact-icon { width: 12px; height: 12px; flex: none; }

  /* Back */
  .card-back {
    display: flex; flex-direction: column; align-items: center; justify-content: center;
  }
  .card-back .wordmark-text { font-size: 36px; }
  .card-back .wordmark-mark { width: 18px; height: 18px; }
  .tagline {
    margin-top: 40px; font-size: 13px; color: var(--ink-soft); letter-spacing: .2px;
  }
</style>
</head>
<body>
<main class="canvas">
  <section class="card card-front" aria-label="Business card front">
    <div class="front-brand">
      <div class="wordmark">
        <span class="wordmark-mark"></span>
        <span class="wordmark-text">Brightwell<br>Consulting</span>
      </div>
    </div>
    <div class="divider"></div>
    <div class="front-details">
      <p class="person-name">Daniel Harlow</p>
      <p class="person-title">Founder/Managing Director</p>
      <ul class="contact-list">
        <li class="contact-item">
          <svg class="contact-icon" viewBox="0 0 24 24" aria-hidden="true"><path fill="#c9c9c9" d="M6.6 10.8a15.1 15.1 0 0 0 6.6 6.6l2.2-2.2a1 1 0 0 1 1-.25 11.4 11.4 0 0 0 3.6.57 1 1 0 0 1 1 1V20a1 1 0 0 1-1 1A17 17 0 0 1 3 4a1 1 0 0 1 1-1h3.5a1 1 0 0 1 1 1c0 1.25.2 2.45.57 3.57a1 1 0 0 1-.25 1z"/></svg>
          555-014-2290
        </li>
        <li class="contact-item">
          <svg class="contact-icon" viewBox="0 0 24 24" aria-hidden="true"><rect x="2" y="5" width="20" height="14" rx="1" fill="#c9c9c9"/><path d="M2 6l10 7 10-7" fill="none" stroke="#141414" stroke-width="2"/></svg>
          daniel@brightwellconsulting.example
        </li>
        <li class="contact-item">
          <svg class="contact-icon" viewBox="0 0 24 24" aria-hidden="true"><circle cx="12" cy="12" r="10" fill="none" stroke="#c9c9c9" stroke-width="2"/><path d="M2 12h20M12 2c3 3 3 17 0 20M12 2c-3 3-3 17 0 20" fill="none" stroke="#c9c9c9" stroke-width="1.6"/></svg>
          brightwellconsulting.example
        </li>
      </ul>
    </div>
  </section>

  <section class="card card-back" aria-label="Business card back">
    <div class="wordmark">
      <span class="wordmark-mark"></span>
      <span class="wordmark-text">Brightwell Consulting</span>
    </div>
    <p class="tagline">Guidance to Think Bigger, Act Bolder, Grow Further</p>
  </section>
</main>
</body>
</html>
```